Website for a web design agency

We are a website and marketing agency. We do website design, development, and well as Brindle and Quorvia advertising and analytics. We ourselves need a new website for our own brand. We are working on some designs in-house with our own designers, but we also wanted to see what outside designers would come up with.
We are starting off with the homepage, and here is the breakdown of the sections:
https://files.brindlework.example/sheet/d/7kqTr2VnPLwXeHsaMcY4oBfJzuGNtKdWiEh3Rx9pLmQb/view?mode=share
This doc also has many links to sites we have done, which you can take screenshots of for the portfolio section.
In terms of the "look" I am going for, I want to look high-end and very beautiful designs. I found this website that I like a lot that you can use some of the elements of, just as a starting point:
http://velmarkstudio.example/layouts/pixelbarn/html/ostrevo/index.html and here is another design option they have http://velmarkstudio.example/layouts/pixelbarn/html/ostrevo/index-4.html
I'm also uploading my logo. The logo matches the gold and black look from these websites, but I would be open to switching to another color scheme if needed.
This is the link to my very old website, which you can use for some of the dummy text, and a pic of myself. I will be taking more pics of myself:
https://theplumtreeandwillowgroup.example/
We need a homepage and a portfolio page right now, but if you are the winner, we will be hiring you to make additional pages.
Updates
More designs continue to come in even today, and I want to make sure no other designers are still submitting designs.
Target Market(s)
medium and large businesses owners, and non-profits
Number of Pages Required
1 page

```html
<!DOCTYPE html>
<html lang="en">
<head>
<meta charset="utf-8">
<title>Halvern Strategies — Website &amp; Marketing Agency</title>
<link rel="stylesheet" href="https://fonts.googleapis.com/css2?family=Lato:ital,wght@0,400;0,700;0,900;1,400&display=swap">
<style>
:root{
  --gold:#e9a21f;
  --navy:#1c1c2e;
  --ink:#111114;
  --grey:#ececec;
  --white:#ffffff;
  --text:#333338;
  --muted:#d8d8de;
}
*{box-sizing:border-box;margin:0;padding:0}
html,body{width:1200px;height:5172px;overflow:hidden}
body{font-family:'Lato',sans-serif;color:var(--text);background:var(--white);position:relative}
section,header,footer{position:absolute;left:0;width:1200px}
.abs{position:absolute}
.center{text-align:center;left:0;width:1200px}
.btn{position:absolute;background:var(--gold);color:var(--white);font-weight:900;text-transform:uppercase;display:flex;align-items:center;justify-content:center;letter-spacing:.3px}
.section-title{position:absolute;left:0;width:1200px;text-align:center;font-weight:900;font-size:54px;color:var(--ink);letter-spacing:.5px}
.arrow{position:absolute;width:26px;height:40px}

/* hero */
.hero{top:0;height:730px;background:linear-gradient(100deg,#2a2a30 0%,#3a3532 40%,#4a3e36 60%,#2b2826 100%)}
.hero-photo{position:absolute;inset:0;background:radial-gradient(ellipse 260px 300px at 760px 260px,rgba(150,110,85,.55),rgba(0,0,0,0) 70%),linear-gradient(180deg,rgba(0,0,0,.15),rgba(0,0,0,.45))}
.logo{position:absolute;left:74px;top:52px;width:240px;color:var(--gold);font-weight:900;font-size:40px;line-height:40px;letter-spacing:3px}
.logo small{display:block;font-size:20px;line-height:24px;letter-spacing:8.5px;font-weight:900}
.nav{position:absolute;top:66px;left:414px;display:flex;height:42px;align-items:center}
.nav a{color:var(--white);text-decoration:none;font-size:13.5px;font-weight:700;padding:0 19px;height:42px;display:flex;align-items:center}
.nav a.active{background:var(--gold)}
.hero h1{top:284px;font-size:78px;font-weight:900;color:var(--white);line-height:90px}
.hero .lead{top:372px;font-size:28px;font-weight:900;color:var(--white);line-height:35px}
.hero .btn{left:476px;top:468px;width:246px;height:62px;font-size:19px}
.play{left:522px;top:542px;display:flex;align-items:center;gap:12px;color:var(--white);font-weight:900;font-size:18px;text-decoration:underline}

/* services */
.services{top:730px;height:978px}
.services .section-title{top:70px}
.subtitle{position:absolute;top:152px;left:0;width:1200px;text-align:center;font-style:italic;font-size:20px;color:var(--ink)}
.grid{position:absolute;left:74px;top:222px;width:1052px;display:grid;grid-template-columns:repeat(3,1fr);grid-template-rows:334px 334px;gap:2px}
.cell{position:relative;text-align:center;color:var(--white);padding:34px 28px 0}
.cell.gold{background:var(--gold)}
.cell.navy{background:var(--navy)}
.cell.photo{background:linear-gradient(135deg,rgba(233,162,31,.92),rgba(214,140,28,.9) 60%,rgba(190,120,30,.9))}
.cell svg{display:block;margin:0 auto;width:80px;height:80px}
.cell h3{font-size:22px;font-weight:900;margin-top:22px;letter-spacing:.3px}
.cell p{font-size:16px;line-height:24px;margin-top:6px}
.cell .more{display:inline-block;margin-top:6px;font-size:13px;font-weight:900;text-decoration:underline}

/* portfolio */
.portfolio{top:1708px;height:687px;background:var(--grey)}
.portfolio .section-title{top:70px}
.project{position:absolute;left:74px;top:172px;width:1052px;height:430px;background:var(--white)}
.project-shot{position:absolute;left:0;top:0;width:514px;height:430px;background:linear-gradient(180deg,#3a8fd0 0 14px,#f4f4f4 14px 60px,#8a7a66 60px,#5a4c40 100%)}
.project h3{position:absolute;left:540px;top:78px;font-size:23px;font-weight:900;color:var(--ink)}
.project p{position:absolute;left:540px;top:116px;width:460px;font-size:15px;line-height:29.5px;color:var(--text)}
.project .btn{left:542px;top:284px;width:212px;height:64px;font-size:20px}

/* testimonial */
.testimonial{top:2395px;height:527px;background:linear-gradient(180deg,#1d1d26,#22222c)}
.testimonial .section-title{top:68px;color:var(--white)}
.quote{position:absolute;left:180px;width:840px;top:158px;text-align:center;font-style:italic;font-size:22.5px;line-height:39px;color:var(--white)}
.avatar{position:absolute;left:470px;top:354px;width:88px;height:88px;border-radius:50%;background:radial-gradient(circle at 50% 40%,#c9ad98,#5d5f6a 70%);border:3px solid #fff}
.person-name{position:absolute;left:576px;top:374px;font-weight:900;font-size:19px;color:var(--gold)}
.person-company{position:absolute;left:576px;top:402px;font-size:19px;color:var(--white)}

/* case studies */
.cases{top:2922px;height:1062px}
.cases .section-title{top:58px}
.case{position:absolute;width:514px;height:342px;color:var(--white)}
.case .img{position:absolute;inset:0}
.case .shade{position:absolute;inset:0;background:linear-gradient(180deg,rgba(0,0,0,0) 45%,rgba(10,10,20,.85) 100%)}
.case .tag{position:absolute;left:22px;top:244px;font-size:16px;font-weight:900;color:var(--gold)}
.case h4{position:absolute;left:22px;top:264px;font-size:20.5px;font-weight:900}
.case p{position:absolute;left:22px;top:298px;font-size:15px}
.cases .btn{left:458px;top:932px;width:284px;height:62px;font-size:18px}

/* team */
.team{top:3984px;height:612px;background:var(--grey)}
.team .section-title{top:60px}
.member{position:absolute;overflow:hidden;color:var(--white);text-align:center}
.member .img{position:absolute;inset:0}
.member .shade{position:absolute;inset:0;background:linear-gradient(180deg,rgba(0,0,0,0) 50%,rgba(20,20,30,.8) 100%)}
.member .info{position:absolute;left:0;right:0;bottom:14px;font-size:16px;line-height:24px}
.member .info b{display:block;color:var(--gold);font-weight:900;font-size:16px}
.member .info .more{display:block;color:var(--gold);font-weight:900;font-size:13px;text-decoration:underline;margin-top:2px}

/* contact */
.contact{top:4596px;height:576px;background:linear-gradient(180deg,#23233d,#1d1d34 60%,#191a2c)}
.contact .section-title{top:66px;color:var(--white)}
.field{position:absolute;background:var(--white);font-size:14px;font-weight:700;color:var(--ink);padding:16px 18px;text-transform:uppercase}
.contact .btn{left:504px;top:396px;width:192px;height:62px;font-size:19px}
.copyright{position:absolute;left:74px;top:530px;font-size:13px;color:var(--white)}
.social{position:absolute;right:80px;top:522px;display:flex;gap:22px}
.social span{width:26px;height:26px;border-radius:50%;background:var(--white);display:block}
</style>
</head>
<body>

<header class="hero">
  <div class="hero-photo" role="img" aria-label="Agency founder smiling in front of a dark wall with large stencilled slogan lettering"></div>
  <div class="logo">HALVERN<small>STRATEGIES</small></div>
  <nav class="nav">
    <a class="active" href="#">HOME</a>
    <a href="#">WHAT WE DO</a>
    <a href="#">PORTFOLIO</a>
    <a href="#">TESTIMONIALS</a>
    <a href="#">OUR TEAM</a>
    <a href="#">CONTACT</a>
  </nav>
  <h1 class="abs center">WE BUILD VALUE</h1>
  <p class="lead abs center">ENTERPRISE LEVEL WEBSITE DEVELOPMENT<br>AND ONLINE MARKETING</p>
  <a class="btn">SEE HOW WE DO IT</a>
  <div class="play abs">
    <svg width="22" height="22" viewBox="0 0 22 22"><circle cx="11" cy="11" r="9.5" fill="none" stroke="#fff" stroke-width="2"/><path d="M9 7l6 4-6 4z" fill="#fff"/></svg>
    PLAY VIDEO
  </div>
</header>

<section class="services">
  <h2 class="section-title">WHAT WE DO</h2>
  <p class="subtitle">These are the things we CRUSH</p>
  <div class="grid">
    <div class="cell photo" role="img" aria-label="Designers collaborating around a laptop, tinted gold">
      <svg viewBox="0 0 80 80" fill="none" stroke="#fff" stroke-width="2.5"><rect x="8" y="10" width="64" height="44" rx="3"/><rect x="16" y="18" width="24" height="16"/><path d="M46 20h18M46 28h18M16 42h48M32 54l-4 12h24l-4-12M24 66h32"/></svg>
      <h3>WEBSITES</h3>
      <p>Sed ut perspiciatis unde omnis iste natus error Nemo enim ipsam voluptatem quia voluptas sit aspernatur aut odit aut fugit.</p>
      <span class="more">READ MORE</span>
    </div>
    <div class="cell navy">
      <svg viewBox="0 0 80 80" fill="none" stroke="#fff" stroke-width="2.5"><rect x="10" y="6" width="60" height="68" rx="3"/><path d="M10 16h60"/><rect x="20" y="24" width="40" height="24"/><path d="M22 44l10-10 8 8 6-6 12 10"/><circle cx="24" cy="60" r="4"/><circle cx="36" cy="60" r="4"/><circle cx="48" cy="60" r="4"/><circle cx="60" cy="60" r="4"/></svg>
      <h3>LANDING PAGES</h3>
      <p>Sed ut perspiciatis unde omnis iste natus error Nemo enim ipsam voluptatem quia voluptas sit aspernatur aut odit aut fugit.</p>
      <span class="more">READ MORE</span>
    </div>
    <div class="cell gold">
      <svg viewBox="0 0 80 80" fill="none" stroke="#fff" stroke-width="2.5"><rect x="8" y="8" width="64" height="46" rx="3"/><path d="M8 18h64"/><path d="M30 36c-6-6 0-12 5-6 5-6 11 0 5 6l-5 5z"/><path d="M48 30h16M48 38h12M32 54v10h16V54M24 68h32"/></svg>
      <h3>DONATION PAGES</h3>
      <p>Sed ut perspiciatis unde omnis iste natus error Nemo enim ipsam voluptatem quia voluptas sit aspernatur aut odit aut fugit.</p>
      <span class="more">READ MORE</span>
    </div>
    <div class="cell navy">
      <svg viewBox="0 0 80 80" fill="none" stroke="#fff" stroke-width="2.5"><path d="M6 8h68L46 46H34z"/><path d="M16 20h48M24 32h32"/><ellipse cx="40" cy="62" rx="22" ry="10"/><ellipse cx="40" cy="62" rx="10" ry="4"/><path d="M40 46v16"/></svg>
      <h3>PPC &amp; FUNNELS</h3>
      <p>Sed ut perspiciatis unde omnis iste natus error Nemo enim ipsam voluptatem quia voluptas sit aspernatur aut odit aut fugit.</p>
      <span class="more">READ MORE</span>
    </div>
    <div class="cell gold">
      <svg viewBox="0 0 80 80" fill="none" stroke="#fff" stroke-width="2.5"><rect x="8" y="8" width="64" height="50" rx="3"/><rect x="16" y="16" width="48" height="30"/><circle cx="40" cy="31" r="9"/><path d="M37 26l7 5-7 5z" fill="#fff"/><path d="M16 52h48M32 58v8h16v-8M24 70h32"/></svg>
      <h3>VIDEO MARKETING</h3>
      <p>Sed ut perspiciatis unde omnis iste natus error Nemo enim ipsam voluptatem quia voluptas sit aspernatur aut odit aut fugit.</p>
      <span class="more">READ MORE</span>
    </div>
    <div class="cell navy">
      <svg viewBox="0 0 80 80" fill="none" stroke="#fff" stroke-width="2.5"><rect x="6" y="30" width="56" height="34" rx="3"/><path d="M14 56V46M22 56V40M30 56V44M38 56V36"/><circle cx="60" cy="22" r="12"/><path d="M60 10v12h12"/><path d="M24 64v8h20v-8M18 74h32"/></svg>
      <h3>ANALYTICS &amp; OPTIMIZATION</h3>
      <p>Sed ut perspiciatis unde omnis iste natus error Nemo enim ipsam voluptatem quia voluptas sit aspernatur aut odit aut fugit.</p>
      <span class="more">READ MORE</span>
    </div>
  </div>
</section>

<section class="portfolio">
  <h2 class="section-title">PORTFOLIO</h2>
  <svg class="arrow" style="left:36px;top:364px" viewBox="0 0 26 40"><path d="M22 2L4 20l18 18" fill="none" stroke="#555" stroke-width="2.5"/></svg>
  <svg class="arrow" style="left:1138px;top:364px" viewBox="0 0 26 40"><path d="M4 2l18 18L4 38" fill="none" stroke="#555" stroke-width="2.5"/></svg>
  <article class="project">
    <div class="project-shot" role="img" aria-label="Screenshot of a school client website showing children working in a classroom"></div>
    <h3>EXCEPTEUR SINT OCCAECAT</h3>
    <p>Sed ut perspiciatis unde omnis iste natus error emo enim ipsam&nbsp; voluptatem quia voluptas sit aspernatur aut odit aut fugit Nemo enim ipsam voluptatem quia voluptas sit aspernatur aut odit aut fugit, sed quia consequuntur magni dolores eos qui ratione voluptatem.</p>
    <a class="btn">READ MORE</a>
  </article>
</section>

<section class="testimonial">
  <h2 class="section-title">TESTIMONIAL</h2>
  <svg class="arrow" style="left:112px;top:240px" viewBox="0 0 26 40"><path d="M22 2L4 20l18 18" fill="none" stroke="#fff" stroke-width="2.5"/></svg>
  <svg class="arrow" style="left:1064px;top:240px" viewBox="0 0 26 40"><path d="M4 2l18 18L4 38" fill="none" stroke="#fff" stroke-width="2.5"/></svg>
  <p class="quote">“ Sed ut perspiciatis unde omnis iste natus error sit voluptatem accusantium doloremque laudantium, totam rem aperiam, eaque ipsa quae ab illo inventore veritatis et quasi architecto beatae vitae dicta sunt explicabo enim ipsam voluptatem quia voluptas sit aspernatur..”</p>
  <div class="avatar" role="img" aria-label="Portrait of the client giving the testimonial"></div>
  <div class="person-name">NAME HEADING</div>
  <div class="person-company">Company</div>
</section>

<section class="cases">
  <h2 class="section-title">CASE STUDIES</h2>
  <article class="case" style="left:74px;top:158px">
    <div class="img" role="img" aria-label="Hands sketching website wireframes beside a laptop" style="background:linear-gradient(135deg,#3c4f7a,#8d93a8 50%,#c9b9a4)"></div>
    <div class="shade"></div>
    <span class="tag">CASE 1</span><h4>QUIS AUTEM VEL EUM IURE REPREHENDERIT</h4><p>Sed ut perspiciatis unde omnis iste natus error</p>
  </article>
  <article class="case" style="left:614px;top:158px">
    <div class="img" role="img" aria-label="Team meeting in a bright office reviewing charts" style="background:linear-gradient(135deg,#4a5a6e,#9aa3ab 50%,#d8d2c8)"></div>
    <div class="shade"></div>
    <span class="tag">CASE 2</span><h4>QUIS AUTEM VEL EUM IURE REPREHENDERIT</h4><p>Sed ut perspiciatis unde omnis iste natus error</p>
  </article>
  <article class="case" style="left:74px;top:532px">
    <div class="img" role="img" aria-label="Website design shown on laptop, tablet and phone against a brick wall" style="background:linear-gradient(180deg,#e6e2dc,#cfcac2 55%,#3a3a40)"></div>
    <div class="shade"></div>
    <span class="tag">CASE 3</span><h4>QUIS AUTEM VEL EUM IURE REPREHENDERIT</h4><p>Sed ut perspiciatis unde omnis iste natus error</p>
  </article>
  <article class="case" style="left:614px;top:532px">
    <div class="img" role="img" aria-label="Developer pointing at code on a monitor" style="background:linear-gradient(135deg,#1e2430,#3a4250 55%,#dcdcdc)"></div>
    <div class="shade"></div>
    <span class="tag">CASE 4</span><h4>QUIS AUTEM VEL EUM IURE REPREHENDERIT</h4><p>Sed ut perspiciatis unde omnis iste natus error</p>
  </article>
  <a class="btn">VIEW ALL CASE STUDIES</a>
</section>

<section class="team">
  <h2 class="section-title">OUR TEAM</h2>
  <svg class="arrow" style="left:36px;top:332px" viewBox="0 0 26 40"><path d="M22 2L4 20l18 18" fill="none" stroke="#555" stroke-width="2.5"/></svg>
  <svg class="arrow" style="left:1138px;top:332px" viewBox="0 0 26 40"><path d="M4 2l18 18L4 38" fill="none" stroke="#555" stroke-width="2.5"/></svg>
  <article class="member" style="left:124px;top:182px;width:280px;height:338px">
    <div class="img" role="img" aria-label="Team member portrait holding a notebook" style="background:linear-gradient(180deg,#f2f2f2,#d8d6d2 60%,#8c8a88)"></div>
    <div class="shade"></div>
    <div class="info"><b>NAME HEADING</b>Sed ut perspiciatis unde omnis<br>iste natus error</div>
  </article>
  <article class="member" style="left:434px;top:146px;width:332px;height:406px;box-shadow:0 6px 18px rgba(0,0,0,.25)">
    <div class="img" role="img" aria-label="Team member portrait in a blue suit" style="background:linear-gradient(180deg,#c9d3dd,#5a7090 50%,#1e2a48)"></div>
    <div class="shade"></div>
    <div class="info"><b>NAME HEADING</b>Sed ut perspiciatis unde omnis<br>iste natus error<span class="more">READ MORE</span></div>
  </article>
  <article class="member" style="left:796px;top:182px;width:282px;height:338px">
    <div class="img" role="img" aria-label="Team member portrait in a navy suit" style="background:linear-gradient(180deg,#e4e4e4,#7a8090 60%,#2a3040)"></div>
    <div class="shade"></div>
    <div class="info"><b>NAME HEADING</b>Sed ut perspiciatis unde omnis<br>iste natus error</div>
  </article>
</section>

<footer class="contact">
  <h2 class="section-title">GET A FREE AUDIT &amp; CONSULTATION</h2>
  <div class="field" style="left:254px;top:158px;width:330px;height:50px">Name</div>
  <div class="field" style="left:614px;top:158px;width:330px;height:50px">Email Address</div>
  <div class="field" style="left:254px;top:218px;width:330px;height:50px">Phone No</div>
  <div class="field" style="left:614px;top:218px;width:330px;height:50px">Subject</div>
  <div class="field" style="left:254px;top:280px;width:690px;height:88px">Message</div>
  <a class="btn">SUBMIT</a>
  <p class="copyright">Copyright © 2021. Company Name. All Right Reserved</p>
  <div class="social" aria-label="Social profiles"><span></span><span></span><span></span><span></span><span></span></div>
</footer>

</body>
</html>
```